Design a menu for a Pizza company

I need help designing a color menu for a pizza company. It will be a 9x16" trifold menu (3-panel). I would like to include some photos of pizza, salads, subs, sandwiches, drinks, etc. (no clipart). Attached is an example of an existing menu. I need to make the menu full color. We would like to modernize this menu with full color photos like the attached sample menu. The final files should have editable files so I can edit prices and menu items as needed. I prefer CorelDraw graphics software.

Target Market(s)

General public.

Industry/Entity Type

Restaurant

Font styles to use
Sans Serif

Colors
ec1f27
fffefc
9bcb3b

Requirements
Must have
• Must have photos and editable fonts. I will need to be able to edit the contents of the menu after you provide me with the final files.
Nice to have
• It would be nice to have this menu created in CorelDraw X7 or X8.
Should not have
• Should not have clip art or low resolution photos.

```html
<!DOCTYPE html>
<html lang="en">
<head>
<meta charset="utf-8">
<title>Pizza Restaurant – Menu</title>
<link href="https://fonts.googleapis.com/css2?family=Oswald:wght@500;600&family=Roboto+Condensed:ital,wght@0,400;0,500;0,700;1,400&display=swap" rel="stylesheet">
<style>
  :root {
    --red: #ec1f27;
    --paper: #fffefc;
    --green: #9bcb3b;
    --yellow: #f4e81c;
    --ink: #1b1b1b;
    --black: #111;
    --backdrop: #5c1012;
  }
  * { box-sizing: border-box; margin: 0; padding: 0; }
  html, body { width: 1200px; height: 800px; overflow: hidden; }
  body { background: var(--backdrop); font-family: "Roboto Condensed", sans-serif; color: var(--ink); position: relative; }

  .menu { position: absolute; left: 0; top: 65px; width: 1200px; height: 670px; display: flex; box-shadow: 0 18px 30px rgba(0,0,0,.55); }
  .panel { position: relative; width: 400px; height: 100%; }
  .panel--dinners { background: linear-gradient(to right, var(--paper) 60%, #dcdcdc 100%); }
  .panel--drinks { background: var(--paper); border-left: 1px solid #ccc; }
  .panel--cover { background: var(--red); }

  .heading { position: absolute; width: 270px; text-align: center; font-family: "Oswald", sans-serif; font-weight: 600; font-size: 18px; color: var(--red); line-height: 26px; transform: translateX(-50%); }
  .heading::before, .heading::after { content: ""; position: absolute; left: 0; right: 0; height: 4px; background: linear-gradient(to right, transparent, var(--red) 25%, var(--red) 75%, transparent); opacity: .85; }
  .heading::before { top: -6px; }
  .heading::after { bottom: -5px; }
  .heading--small { font-size: 15px; width: 230px; }

  .note { position: absolute; left: 200px; transform: translateX(-50%); width: 260px; text-align: center; font-style: italic; font-size: 9.5px; line-height: 10.5px; color: #333; }

  .item { position: absolute; font-weight: 500; font-size: 12.5px; line-height: 14px; white-space: nowrap; }
  .priced { position: absolute; display: flex; align-items: baseline; font-weight: 500; font-size: 12.5px; line-height: 14px; white-space: nowrap; }
  .priced .leader { flex: 1; border-bottom: 1.5px dotted var(--ink); margin: 0 3px; transform: translateY(-3px); }
  .row { position: absolute; display: flex; font-weight: 500; font-size: 12.5px; white-space: nowrap; }
  .row .name { width: 128px; display: flex; }
  .row .name .leader { flex: 1; border-bottom: 1.5px dotted var(--ink); margin: 0 3px; transform: translateY(-4px); }
  .row .sizes { width: 160px; display: flex; justify-content: space-between; }
  .label { position: absolute; font-weight: 700; font-size: 14px; }

  .photo { position: absolute; border-radius: 6px; }
  .photo--tenders { left: 280px; top: 462px; width: 120px; height: 60px; background: radial-gradient(ellipse at center, #d89a45, #b86f25 60%, #f2eee6); border-radius: 50%; }
  .photo--fries { left: 331px; top: 511px; width: 66px; height: 70px; background: linear-gradient(#f0b640, #c48a26 70%, #8a8a8a); }
  .photo--splash { left: 647px; top: 8px; width: 153px; height: 69px; background: linear-gradient(to right, transparent, #a4502a 50%, #6a2a14); opacity: .75; }
  .photo--can { left: 731px; top: 79px; width: 69px; height: 135px; background: linear-gradient(to right, #9c0d12, #e2242b 45%, #9c0d12); border-radius: 8px; }
  .photo--beer { left: 647px; top: 337px; width: 138px; height: 285px; background: linear-gradient(to right, #e99a2a 0%, #c86a12 45%, #3b1d10 55%, #1c0e08 100%); border-radius: 10px; }

  .brand { position: absolute; left: 853px; top: 34px; width: 300px; font-family: "Oswald", sans-serif; font-weight: 600; color: var(--yellow); line-height: 1; }
  .brand__name { font-size: 78px; display: block; }
  .brand__sub { font-size: 30px; display: block; margin-left: 120px; margin-top: 2px; }
  .chef { position: absolute; left: 826px; top: 170px; width: 340px; height: 342px; background: radial-gradient(ellipse at 45% 50%, #ffffff 0%, #f3f3f3 40%, rgba(255,255,255,0) 70%); }

  .info-band { position: absolute; left: 800px; top: 512px; width: 400px; height: 158px; background: var(--green); }
  .open-box { position: absolute; left: 1px; top: 34px; width: 111px; height: 110px; background: var(--black); color: #fff; font-family: "Oswald", sans-serif; font-weight: 500; font-size: 24px; line-height: 32px; padding: 6px 0 0 28px; }
  .info-band__edge { position: absolute; right: 0; top: 34px; width: 11px; height: 110px; background: var(--black); }
  .hours { position: absolute; left: 112px; right: 11px; top: 48px; text-align: center; color: var(--black); font-weight: 500; font-size: 12.5px; line-height: 15.5px; }
  .cards { position: absolute; left: 112px; right: 11px; top: 95px; text-align: center; color: #fff; font-weight: 500; font-size: 15px; }
  .service { position: absolute; left: 112px; right: 11px; top: 112px; text-align: center; color: var(--yellow); font-family: "Oswald", sans-serif; font-weight: 500; font-size: 24px; }
</style>
</head>
<body>
<main class="menu">

  <section class="panel panel--dinners">
    <h2 class="heading" style="left:200px; top:28px;">ITALIAN DINNERS</h2>
    <p class="note" style="top:63px;">Served on Garlic Bread &amp; Salad<br>Choice of Dressing :<br>Ranch, French, Italian, Blue Cheese, Thousand Island</p>
    <p class="item" style="left:31px; top:106px;">Spaghetti w/ Meat Sauce</p>
    <p class="item" style="left:31px; top:133px;">Spaghetti w/ Meatballs</p>
    <p class="item" style="left:31px; top:160px;">Veal Parmigiana w/ Spaghetti</p>
    <p class="item" style="left:31px; top:187px;">Chicken Parmigiana w/ Spaghetti</p>
    <p class="item" style="left:31px; top:213px;">Eggplant Parmigiana w/ Spaghetti</p>
    <p class="item" style="left:31px; top:240px;">Baked Lasagna</p>
    <p class="item" style="left:31px; top:266px;">Ravioli w/ Meat Sauce</p>

    <h2 class="heading" style="left:200px; top:289px;">SEAFOOD DINNERS</h2>
    <p class="note" style="top:324px;">Served with Garlic Bread, French Fries &amp; Salad<br>Choice of Dressing :<br>Ranch, French, Italian, Blue Cheese, Thousand Island</p>
    <p class="item" style="left:31px; top:372px;">Shrimp Basket</p>
    <p class="item" style="left:31px; top:398px;">Crab Cake</p>
    <p class="item" style="left:31px; top:423px;">Fish Filet</p>

    <h2 class="heading" style="left:200px; top:446px;">CHILDREN'S MENU</h2>
    <p class="priced" style="left:31px; width:244px; top:478px;">Chicken Tenders w/ French Fries<span class="leader"></span>5.99</p>
    <p class="priced" style="left:31px; width:244px; top:504px;">Spaghetti w/ Meat Sauce<span class="leader"></span>5.99</p>
    <p class="priced" style="left:31px; width:244px; top:530px;">Ravioli w/ Meat Sauce<span class="leader"></span>5.99</p>
    <p class="priced" style="left:31px; width:244px; top:556px;">Shrimp w/ French Fries<span class="leader"></span>5.99</p>
    <p class="priced" style="left:31px; width:300px; top:583px;">*Cheeseburger w/ French Fries &amp; small Beverage<span class="leader"></span>5.99</p>
    <p class="note" style="top:611px;">* These items are cooked to order.<br>"Consuming raw or undercooked meats may increase<br>your risk of foodborne illness."</p>

    <div class="photo photo--tenders" role="img" aria-label="Photo of chicken tenders with fries and dipping sauce"></div>
    <div class="photo photo--fries" role="img" aria-label="Photo of french fries in a cup"></div>
  </section>

  <section class="panel panel--drinks">
    <h2 class="heading" style="left:200px; top:28px;">SODA</h2>
    <p class="priced" style="left:29px; width:155px; top:62px;">PITCHER<span class="leader"></span>3.99</p>
    <div class="row" style="left:29px; top:87px;"><span class="name">RED COLA</span><span class="sizes" style="width:160px;"><span>12 oz.</span><span>16 oz.</span><span>24 oz.</span><span>32 oz.</span></span></div>
    <div class="row" style="left:29px; top:111px;"><span class="name">RED COLA<span class="leader"></span></span><span class="sizes"><span>&nbsp;&nbsp;99</span><span>1.30</span><span>1.69</span><span>1.99</span></span></div>
    <div class="row" style="left:29px; top:136px;"><span class="name">CITRUS FIZZ<span class="leader"></span></span><span class="sizes"><span>&nbsp;&nbsp;99</span><span>1.30</span><span>1.69</span><span>1.99</span></span></div>
    <div class="row" style="left:29px; top:161px;"><span class="name">ROOT BEER<span class="leader"></span></span><span class="sizes"><span>&nbsp;&nbsp;99</span><span>1.30</span><span>1.69</span><span>1.99</span></span></div>
    <div class="row" style="left:29px; top:186px;"><span class="name">DIET RED COLA<span class="leader"></span></span><span class="sizes"><span>&nbsp;&nbsp;99</span><span>1.30</span><span>1.69</span><span>1.99</span></span></div>

    <div class="photo photo--splash" role="img" aria-label="Photo of a cola splash with bottle and glass"></div>
    <div class="photo photo--can" role="img" aria-label="Photo of a red cola can"></div>

    <h2 class="heading" style="left:200px; top:211px;">BEVERAGES</h2>
    <p class="priced" style="left:29px; width:350px; top:246px;">ICED TEA<span class="leader"></span>16 oz. ...... 24 oz. ...... 32 oz.</p>
    <p class="item" style="left:221px; top:271px;">1.30 &nbsp;...... &nbsp;1.69 &nbsp;...... &nbsp;1.99</p>

    <h2 class="heading" style="left:200px; top:298px;">BEER</h2>
    <p class="label" style="left:29px; top:329px;">DRAFT</p>
    <p class="priced" style="left:29px; width:197px; top:356px;">32 OZ. PITCHER<span class="leader"></span>6.99</p>
    <p class="priced" style="left:29px; width:197px; top:381px;">60 OZ. PITCHER<span class="leader"></span>10.99</p>
    <p class="priced" style="left:29px; width:197px; top:405px;">BRADFORD<span class="leader"></span>2.60</p>

    <h3 class="heading heading--small" style="left:127px; top:427px;">BOTTLES</h3>
    <p class="priced" style="left:29px; width:197px; top:456px;">BRADFORD<span class="leader"></span>3.25</p>
    <p class="priced" style="left:29px; width:197px; top:481px;">MILLSTONE<span class="leader"></span>3.25</p>
    <p class="priced" style="left:29px; width:197px; top:506px;">MILLSTONE LITE<span class="leader"></span>3.25</p>
    <p class="priced" style="left:29px; width:197px; top:530px;">CORDELL<span class="leader"></span>3.25</p>
    <p class="priced" style="left:29px; width:197px; top:555px;">CORDELL LIGHT<span class="leader"></span>3.25</p>

    <h3 class="heading heading--small" style="left:127px; top:578px;">IMPORTED BOTTLES</h3>
    <p class="priced" style="left:29px; width:197px; top:605px;">HOLLANDER<span class="leader"></span>3.75</p>
    <p class="priced" style="left:29px; width:197px; top:630px;">CORALINA<span class="leader"></span>3.75</p>
  </section>

  <section class="panel panel--cover"></section>

  <div class="photo photo--beer" role="img" aria-label="Photo of a glass of amber beer beside a beer bottle"></div>

  <h1 class="brand"><span class="brand__name">Pizza</span><span class="brand__sub">Restaurant</span></h1>
  <div class="chef" role="img" aria-label="Illustration of a pizza chef tossing dough"></div>

  <div class="info-band">
    <p class="open-box">OPEN<br>7 DAYS<br>A WEEK</p>
    <div class="info-band__edge"></div>
    <p class="hours">MONDAY - THURSDAY | 10:30 A.M. - 9:30 P.M.<br>FRIDAY &amp; SATURDAY | 10:30 A.M.- 10:00 P.M.<br>SUNDAY | 12:00 NOON - 8:00 P.M.</p>
    <p class="cards">Major Credit Cards Accepted</p>
    <p class="service">DINE-IN and CARRY OUT</p>
  </div>

</main>
</body>
</html>
```